IT Services, Internet & Telephone Brochure

We need a new brochure that captures our core services. We have attached a pdf made in powerpoint providing the majority of content we would like. We have also included our telephone brochure as a example of colors and design that we liked. Lastly, we would like the designer to take liberty in developing a clean, professional but eye catching design.

```html
<!DOCTYPE html>
<html lang="en">
<head>
<meta charset="utf-8">
<title>nexora – IT, Internet &amp; Telephone</title>
<link rel="stylesheet" href="https://fonts.googleapis.com/css2?family=Montserrat:wght@300;500;600;700&family=Open+Sans:wght@400;600;700&family=Roboto+Condensed:wght@400&display=swap">
<style>
:root{
  --navy:#2b3580;
  --orange:#f26522;
  --sky:#3db4e8;
  --ink:#1e1e1e;
  --white:#ffffff;
  --bar:rgba(25,30,40,.78);
}
*{margin:0;padding:0;box-sizing:border-box}
html,body{width:960px;height:1200px;overflow:hidden;background:#fff}
.flyer{position:relative;width:960px;height:1200px;font-family:"Open Sans",sans-serif;color:var(--ink);overflow:hidden}
.hero{position:absolute;left:0;top:0;width:960px;height:472px;
  background:linear-gradient(160deg,#6f8fae 0%,#3f6f9c 35%,#27507e 60%,#4a86b8 85%,#7fb2d6 100%)}
.headline{position:absolute;left:88px;top:82px;color:var(--white);font-family:"Montserrat",sans-serif;line-height:1.1}
.headline .light{font-weight:300;font-size:41px;letter-spacing:.5px}
.headline .bold{font-weight:700;font-size:41px;display:block;margin-top:4px}
.brand{position:absolute;right:72px;top:62px;color:var(--white);font-family:"Montserrat",sans-serif;font-weight:600;font-size:72px;letter-spacing:-2px;line-height:1;text-align:right}
.tagline{position:absolute;right:72px;top:164px;color:var(--white);font-family:"Roboto Condensed",sans-serif;font-size:15px;text-align:right}
.service{position:absolute;left:90px;height:62px;display:flex;align-items:center}
.service .icon{width:62px;height:62px;background:var(--white);display:flex;align-items:center;justify-content:center;margin-right:8px}
.service .label{height:62px;background:var(--bar);color:var(--white);font-family:"Montserrat",sans-serif;font-weight:500;font-size:26px;letter-spacing:.5px;display:flex;align-items:center;padding:0 28px}
.section-head{position:absolute;left:0;width:960px;height:54px}
.section-head .head-band{position:absolute;left:0;top:0}
.section-head .badge{position:absolute;left:35px;top:-4px;width:62px;height:62px;border-radius:50%;background:var(--orange);border:3px solid #fff;box-shadow:0 0 0 2px var(--orange);display:flex;align-items:center;justify-content:center}
.section-head h2{position:absolute;left:116px;top:7px;color:var(--white);font-family:"Montserrat",sans-serif;font-weight:600;font-size:33px;letter-spacing:1px}
.section-head .price{position:absolute;left:530px;top:7px;color:var(--white);font-family:"Montserrat",sans-serif;font-weight:600;font-size:33px}
.sub{position:absolute;left:86px;color:var(--orange);font-weight:700;font-size:14px}
.ticks{position:absolute;list-style:none;font-size:14px;line-height:23.5px}
.ticks li{padding-left:18px;position:relative;white-space:nowrap}
.ticks li::before{content:"✓";position:absolute;left:0;color:var(--orange);font-weight:700}
.para{position:absolute;font-size:14px;line-height:19.5px}
.link{color:var(--orange);font-weight:700}
.speed{color:var(--navy);font-weight:700}
.rate{color:var(--orange);font-weight:700}
.note{position:absolute;font-size:12px}
.footer{position:absolute;left:0;top:1134px;width:960px;height:66px}
.footer .foot-band{position:absolute;left:0;top:0}
.footer .item{position:absolute;top:0;height:66px;color:var(--white);font-family:"Montserrat",sans-serif;font-weight:500;font-size:23px;display:flex;align-items:center;gap:8px;white-space:nowrap}
.footer .item svg{flex:none}
</style>
</head>
<body>
<div class="flyer">
  <section class="hero" role="img" aria-label="Upward view of glass office towers against a blue sky">
    <div class="headline"><span class="light">MORE THAN JUST</span><span class="bold">ANOTHER IT COMPANY</span></div>
    <div class="brand">nexora</div>
    <div class="tagline">Internet-Telephone-Security-Networking</div>

    <div class="service" style="top:218px">
      <div class="icon"><svg width="34" height="34" viewBox="0 0 34 34" fill="none" stroke="#f26522" stroke-width="2"><path d="M9 14a6 6 0 0 1 11-4 5 5 0 0 1 6 6H9z"/><rect x="9" y="18" width="16" height="4"/><rect x="9" y="24" width="16" height="4"/></svg></div>
      <div class="label">MANAGED IT SERVICES</div>
    </div>
    <div class="service" style="top:294px">
      <div class="icon"><svg width="34" height="34" viewBox="0 0 34 34" fill="none" stroke="#f26522" stroke-width="2"><path d="M8 9c-3 3 2 12 7 16s10 5 12 2l-4-4-3 2c-2-1-5-4-6-6l2-3-4-4z"/><circle cx="22" cy="12" r="7"/></svg></div>
      <div class="label">HOSTED BUSINESS VOIP SERVICES</div>
    </div>
    <div class="service" style="top:370px">
      <div class="icon"><svg width="34" height="34" viewBox="0 0 34 34" fill="none" stroke="#f26522" stroke-width="2"><path d="M7 29l8-10M15 19l-5-9M15 19l10-9M15 19l12 3"/><circle cx="10" cy="8" r="2"/><circle cx="26" cy="8" r="2"/><circle cx="28" cy="22" r="2"/></svg></div>
      <div class="label">HIGH SPEED FIBER INTERNET SERVICE</div>
    </div>
  </section>

  <div class="section-head" style="top:494px">
    <svg class="head-band" width="960" height="54"><polygon points="80,0 520,0 550,52 80,52" fill="var(--navy)"/><polygon points="483,0 735,0 768,52 515,52" fill="var(--orange)"/><rect x="768" y="50" width="192" height="2" fill="var(--orange)"/></svg>
    <div class="badge"><svg width="32" height="32" viewBox="0 0 32 32" fill="none" stroke="#fff" stroke-width="2"><rect x="4" y="6" width="6" height="20" rx="2"/><rect x="12" y="8" width="16" height="18" rx="1"/><rect x="15" y="11" width="10" height="4"/><path d="M15 19h2M19 19h2M23 19h2M15 22h2M19 22h2M23 22h2"/></svg></div>
    <h2>PHONE SERVICES</h2>
    <div class="price">$19.95/MO</div>
  </div>
  <div class="sub" style="top:560px">Telephone Options:</div>
  <ul class="ticks" style="left:70px;top:582px">
    <li>Vantel V23 with three-way audio calling, 2.8” Black &amp; White LCD Display, 3 programmable keys, wired headset support, etc.</li>
    <li>Vantel V29 with three-way audio calling, 4.3” Color LCD Display, 10 programmable keys, wireless headset support, etc.</li>
  </ul>
  <div class="sub" style="top:637px">Telephone Pricing Options:</div>
  <ul class="ticks" style="left:70px;top:658px">
    <li>Vantel V23 purchase for $75 each or monthly rental of $2.00/mo</li>
    <li>Vantel V29 purchase for $135 each or monthly rental of $3.50/mo</li>
  </ul>
  <p class="para" style="left:86px;top:711px;width:770px">Business Telephone Features: Caller-ID, Call Forwarding, Call Transfer, Virtual Assistance/Auto Attendant,<br>Simultaneous Ring, Mobile App,1-line per phone included, 1 telephone number per phone included and much more.<br><span class="link">For more information head to www.nexorait.com.</span></p>

  <div class="section-head" style="top:783px">
    <svg class="head-band" width="960" height="54"><polygon points="80,0 655,0 688,52 80,52" fill="var(--navy)"/><polygon points="655,0 665,0 698,52 688,52" fill="var(--orange)"/><rect x="698" y="50" width="262" height="2" fill="var(--orange)"/></svg>
    <div class="badge"><svg width="32" height="32" viewBox="0 0 34 34" fill="none" stroke="#fff" stroke-width="2.2"><path d="M7 29l8-10M15 19l-5-9M15 19l10-9M15 19l12 3"/><circle cx="10" cy="8" r="2"/><circle cx="26" cy="8" r="2"/><circle cx="28" cy="22" r="2"/></svg></div>
    <h2>HIGH SPEED FIBER INTERNET</h2>
  </div>
  <div class="sub" style="top:844px">Bandwidth Options:</div>
  <ul class="ticks" style="left:70px;top:866px;line-height:22.5px">
    <li><span class="speed">100Mbps</span> starting at <span class="rate">$135/mo</span></li>
    <li><span class="speed">150Mbps</span> starting at <span class="rate">$185/mo</span></li>
  </ul>
  <div class="note" style="left:86px;top:917px">*Price varies depending on location</div>
  <p class="para" style="left:398px;top:868px;width:460px">Features/Benefits: Dedicated symmetrical uplink &amp; downlink speeds,<br>no slow down during peak times, 99.99% uptime guarantee, static<br>IP address, local support.</p>

  <div class="section-head" style="top:947px">
    <svg class="head-band" width="960" height="54"><polygon points="80,0 465,0 497,52 80,52" fill="var(--navy)"/><polygon points="465,0 475,0 507,52 497,52" fill="var(--orange)"/><rect x="507" y="50" width="453" height="2" fill="var(--orange)"/></svg>
    <div class="badge"><svg width="32" height="32" viewBox="0 0 32 32" fill="none" stroke="#fff" stroke-width="2"><rect x="6" y="6" width="20" height="14"/><path d="M3 24h26"/><path d="M16 8l5 2v4c0 2-2 4-5 5-3-1-5-3-5-5v-4z"/></svg></div>
    <h2>IT SERVICES</h2>
  </div>
  <ul class="ticks" style="left:70px;top:1010px;line-height:21px">
    <li>PC Protection</li><li>Server Protection</li><li>Backups &amp; Disaster Recovery</li><li>Email/Spam Protection</li>
  </ul>
  <ul class="ticks" style="left:363px;top:1010px;line-height:21px">
    <li>PC &amp; Network Hardware Sales</li><li>Software Sales</li><li>Consulting</li><li>Cloud Services</li>
  </ul>
  <ul class="ticks" style="left:667px;top:1010px;line-height:21px">
    <li>Ransomware Protection</li><li>Cloud Office Suite</li><li>Troubleshooting/Repair</li><li>WiFi</li>
  </ul>
  <div class="note" style="left:70px;top:1106px">*Standard hourly rate $75/hr or customized monthly rate for all services</div>

  <footer class="footer">
    <svg class="foot-band" width="960" height="66"><rect width="960" height="66" fill="var(--orange)"/><polygon points="0,0 360,0 328,66 0,66" fill="var(--sky)"/><polygon points="360,0 688,0 656,66 328,66" fill="var(--navy)"/></svg>
    <div class="item" style="left:58px"><svg width="20" height="20" viewBox="0 0 20 20" fill="none" stroke="#fff" stroke-width="1.6"><circle cx="10" cy="10" r="8"/><ellipse cx="10" cy="10" rx="3.5" ry="8"/><path d="M2 10h16"/></svg>www.nexorait.com</div>
    <div class="item" style="left:376px"><svg width="20" height="16" viewBox="0 0 20 16" fill="none" stroke="#fff" stroke-width="1.6"><rect x="1" y="1" width="18" height="14"/><path d="M1 1l9 8 9-8"/></svg>sales@nexorait.com</div>
    <div class="item" style="left:700px"><svg width="20" height="20" viewBox="0 0 20 20" fill="none" stroke="#fff" stroke-width="1.6"><circle cx="10" cy="10" r="8.5"/><path d="M7 5.5l2 2-1 1.5c.5 1.2 1.8 2.5 3 3l1.5-1 2 2-1.5 1.5c-3 0-7-4-7-7z"/></svg>555.014.2290</div>
  </footer>
</div>
</body>
</html>
```